Dental Practice - Smiles Ahead - Corvell Walk - requires New Patient Flyer

We need a flyer to tell prospecting new patients about a new patient offer in our practice, Themed with black and whitewith a bit of colour, and using black and white stripes if possible.
We want to look empathetic, modern and appeal to adults.
The offer is for a complete comprehensive dental examination including all necessary x-rays with no out of pocket expense

Target Market(s)

adults, in particular 30-60 year olds

Industry/Entity Type

Dental

Font styles to use
Sans Serif

Colors
000000
ffffff
cee9f5

Requirements
Must have
• Smiles Ahead
• We are located in the heart of city Adelaide, along the iconic Corvell Walk.
• Dentist
• Complete comprehensive dental examination including all necessary x-rays
• with $0 out of pocket expense if you have dental health cover.
• No Health fund? We will do it all for you $95.
• With over 50 years combined experience, Dr Peter Halvorsen and Dr Wesley Tunbridge can offer all areas of dental treatment including Preventative, Whitening, Children, General, Cosmetic, Removal, Sedation and Implants.
• (08) 8564 3097
• frontdesk@brightquaydental.com.au
• Level 2, 17 Corvell Walk Adelaide SA 5000
• Please try and include all 3 pictures attached
Nice to have
• Partner Plus with KOVA, Accept all health funds, claim on the spot with MEDSWIPE
Should not have
• colour red, someone not smiling, someone in pain, photo of bad teeth/smile

```html
<!DOCTYPE html>
<html lang="en">
<head>
<meta charset="utf-8">
<title>Smiles Ahead – New Patient Flyer</title>
<link href="https://fonts.googleapis.com/css2?family=PT+Sans:ital,wght@0,400;0,700;1,400;1,700&family=PT+Sans+Narrow:wght@700&display=swap" rel="stylesheet">
<style>
  :root {
    --ink: #000000;
    --paper: #ffffff;
    --sky: #cee9f5;
    --sky-deep: #3f93d2;
    --silver-light: #f4f4f4;
    --silver-mid: #c9c9c9;
    --silver-dark: #8e8e8e;
    --band-dark: #141414;
    --band-mid: #3a3a3a;
    --partner-blue: #1c8fd6;
    --map-tone: #d9d9d9;
  }
  * { margin: 0; padding: 0; box-sizing: border-box; }
  html, body { width: 847px; height: 1200px; overflow: hidden; background: var(--paper); }
  .flyer {
    position: relative; width: 847px; height: 1200px; overflow: hidden;
    background: linear-gradient(135deg, var(--silver-light), var(--silver-dark) 30%, var(--silver-light) 55%, var(--silver-mid) 80%, var(--silver-dark));
    font-family: "PT Sans", Arial, sans-serif; color: var(--ink);
  }
  .sheet {
    position: absolute; left: 20px; top: 20px; width: 807px; height: 1160px; overflow: hidden;
    background: linear-gradient(180deg, var(--paper) 0%, #f1f1f1 60%, var(--paper) 100%);
    box-shadow: inset 0 0 6px rgba(0,0,0,.35);
  }
  .photo-area { position: absolute; inset: 0; }
  .tilt { position: absolute; transform-origin: 0 0; white-space: nowrap; }

  .offer { left: 30px; top: 66px; transform: rotate(-11deg); }
  .offer-question {
    font-family: "PT Sans Narrow", "Arial Narrow", sans-serif; font-weight: 700;
    font-size: 64px; line-height: .86; text-transform: uppercase; letter-spacing: -1px;
  }
  .offer-question .line-two { padding-left: 20px; }
  .offer-question .line-three { padding-left: 42px; }
  .offer-price {
    margin-top: 10px; padding-left: 60px;
    font-family: "PT Sans Narrow", "Arial Narrow", sans-serif; font-weight: 700;
    font-size: 30px; line-height: 1; text-transform: uppercase;
  }
  .offer-detail { margin-top: 12px; padding-left: 62px; font-weight: 700; font-size: 18px; line-height: 1.05; }
  .offer-note { padding-left: 190px; font-style: italic; font-size: 14px; }

  .whitening { left: 560px; top: 46px; transform: rotate(-8deg); text-align: center; line-height: 1; }
  .whitening-get { font-family: "PT Sans Narrow", "Arial Narrow", sans-serif; font-weight: 700; font-size: 28px; }
  .whitening-wow { font-family: "PT Sans Narrow", "Arial Narrow", sans-serif; font-weight: 700; font-size: 38px; }
  .whitening-rest { font-weight: 700; font-size: 15px; text-transform: uppercase; }

  /* Everything below shares one slanted frame so text sits on its band */
  .slant {
    position: absolute; left: -20px; top: 565px; width: 0; height: 0;
    transform: rotate(-14deg); transform-origin: 0 0;
  }
  .slant > * { position: absolute; white-space: nowrap; }
  .band { left: -400px; width: 1700px; }
  .rule { background: linear-gradient(180deg, #e2e2e2, var(--silver-dark)); }
  .band-dark { background: linear-gradient(180deg, var(--band-mid), var(--band-dark) 50%, #262626); }
  .band-light { background: linear-gradient(180deg, #f7f7f7, #dcdcdc); }

  .brand { left: 120px; top: -72px; font-weight: 700; font-size: 46px; line-height: 56px; }

  .rule-top { top: -12px; height: 12px; }
  .band-services { top: 0; height: 250px; }
  .rule-mid { top: 250px; height: 12px; }
  .band-gap { top: 262px; height: 38px; }
  .band-funds { top: 300px; height: 64px; }
  .rule-low { top: 364px; height: 10px; }

  .experience { left: 140px; top: 88px; color: var(--paper); font-size: 19px; line-height: 26px; }
  .services { margin-top: 12px; font-size: 22px; line-height: 29px; }
  .services .row-one { padding-left: 0; }
  .services .row-two { padding-left: 150px; }

  .funds { left: 10px; top: 300px; line-height: 64px; color: var(--paper); font-weight: 700; font-size: 18px; text-transform: uppercase; }

  .contact { left: -60px; top: 428px; font-size: 19px; line-height: 28px; text-transform: uppercase; }
  .contact strong { font-weight: 700; }
  .contact .located { padding-left: 40px; }
  .contact .address { padding-left: 120px; font-weight: 700; font-size: 22px; line-height: 30px; }

  .partner {
    left: 600px; top: 500px; width: 96px; height: 74px;
    background: var(--paper); border: 1px solid var(--silver-mid);
    display: flex; flex-direction: column; align-items: center; justify-content: center; gap: 4px;
    color: var(--partner-blue); font-weight: 700; font-size: 11px; line-height: 1.1; text-transform: uppercase; text-align: center;
  }
  .partner-mark { width: 26px; height: 26px; background: var(--partner-blue); }

  .map { left: 300px; top: 545px; width: 200px; height: 92px; background: var(--map-tone); border: 2px solid var(--paper); }
</style>
</head>
<body>
<div class="flyer">
  <div class="sheet">
    <svg class="photo-area" width="807" height="1160" viewBox="0 0 807 1160">
      <defs>
        <linearGradient id="frameBlue" x1="0" y1="0" x2="1" y2="1">
          <stop offset="0" stop-color="#cee9f5"/>
          <stop offset=".5" stop-color="#3f93d2"/>
          <stop offset="1" stop-color="#1d5f9e"/>
        </linearGradient>
        <linearGradient id="photoTone" x1="0" y1="0" x2="1" y2="1">
          <stop offset="0" stop-color="#cee9f5"/>
          <stop offset=".45" stop-color="#b58a70"/>
          <stop offset="1" stop-color="#5a3a2c"/>
        </linearGradient>
      </defs>
      <polygon points="522,0 807,0 807,362 334,480" fill="url(#frameBlue)"/>
      <polygon role="img" aria-label="Photo of a smiling woman with bright white teeth" points="540,0 807,0 807,362 352,476" fill="url(#photoTone)"/>
    </svg>

    <div class="tilt offer">
      <div class="offer-question">
        <div>No</div>
        <div class="line-two">Health</div>
        <div class="line-three">Fund?</div>
      </div>
      <div class="offer-price">We will do it all<br>for you for only $95!</div>
      <div class="offer-detail">Complete comprehensive dental<br>examination including all necessary<br>x-rays with $0 out of pocket expense</div>
      <div class="offer-note">if you have dental health coverage.</div>
    </div>

    <div class="tilt whitening">
      <div class="whitening-get">GET</div>
      <div class="whitening-wow">“WOW”</div>
      <div class="whitening-rest">Whitening results,<br>today!</div>
    </div>

    <div class="slant">
      <div class="brand">Smiles Ahead</div>

      <div class="band rule rule-top"></div>
      <div class="band band-dark band-services"></div>
      <div class="band rule rule-mid"></div>
      <div class="band band-light band-gap"></div>
      <div class="band band-dark band-funds"></div>
      <div class="band rule rule-low"></div>

      <div class="experience">
        <div>With over 50 years combined experience, Dr Peter Halvorsen<br>and Dr Wesley Tunbridge can offer all areas of dental treatment including:</div>
        <div class="services">
          <div class="row-one"><strong>Preventative</strong> | Whitening | <strong>Children</strong> | General | <strong>Cosmetic</strong></div>
          <div class="row-two">Removal | <strong>Sedation</strong> | Implants</div>
        </div>
      </div>

      <div class="funds">We accept all health funds! &nbsp;|&nbsp; Get a claim on the spot with MEDSWIPE!</div>

      <div class="contact">
        <div><strong>Phone:</strong> (08) 8564 3097 | <strong>E-mail:</strong> frontdesk@brightquaydental.com.au</div>
        <div class="located">Located in the heart of city Adelaide, along the iconic Corvell Walk.</div>
        <div class="address">Level 2, 17 Corvell Walk Adelaide SA 5000</div>
      </div>

      <div class="partner">
        <span class="partner-mark"></span>
        <span>KOVA<br>Partner Plus</span>
      </div>

      <div class="map" role="img" aria-label="Street map showing the clinic location on Corvell Walk"></div>
    </div>
  </div>
</div>
</body>
</html>
```